Healthy Snack Bar Wrapper Design

We are passionate about delivering healthy and tasty treats that are Raw, Organic, Preservative Free, Gluten Free, have No Added Sugar and No Additives!
In this project we are looking for a design for a new healthy food product to be launched soon in Australia. The packaging will be a bar wrapper made from foil that will be hot sealed, with a front and a back.
The snack is a raw, organic and healthy treat made predominantly with nuts, and will come in 3 initial flavours:
- Velvet Harbor (Sour Cherry and Choc)
- Plum Fizzaroo (Banana, Apricot and Blueberry)
- Sunmelodia (Pineapple, Passionfruit and Kiwi)
The product name is MunchWell, which does not currently have a logo. We are happy to have this as a simple written component of the initial design at the top of the packaging, perhaps within an circle, square or oval.
The typeface used for the names and the main ingredients should be fun.
The overall design should be very simple and make use of minimal colours. Our preferences are to have a plain colour for the background, such as light organic brown or white, with an eye catching colour that can be used to define the flavour, but should not be too vibrant.
We do not want to have an 3 dimensional images or objects. Nor do we want to have product images and any imagery should be only to give the impression of the flavours within rather than an image of the flavour. Finally, we do not want to have gradients included in the design.
The final design should communicate healthy, tasty and fun!
Examples of inspiration designs are attached in the files.
Main Information:
- The front should comprise of the following information:
-- MunchWell
-- Flavour name (such as Velvet Harbor)
-- Main Ingredients (Sour Cherry and Choc) (This is optional)
-- Portion size (60g)
-- Message (This is optional)
--- 0% Additives
--- 60% Nuts
--- 100% Natural
- The back needs to have space for the following information:
-- Nutritional Information
-- Barcode
-- Ingredients
-- Contact information
- Wrapper Dimensions
-- Width: 14cm
-- Height: 15cm
- Bar Dimensions
-- Width: 3cm
-- Height: 10cm
-- Depth: 2.5cm
Target Market(s)
People who want to have a healthy tasty treat
Colors
Designer to choose colors to be used in the design.
Requirements
Must have
- Main Information:
- - The front should comprise of the following information:
- -- MunchWell
- -- Flavour name (such as Velvet Harbor)
- -- Main Ingredients (Sour Cherry and Choc) (This is optional)
- -- Portion size (60g)
- -- Message (This is optional)
- --- 0% Additives
- --- 60% Nuts
- --- 100% Natural
- - The back needs to have space for the following information:
- -- Nutritional Information
- -- Barcode
- -- Ingredients
- -- Contact information
- - Wrapper Dimensions
- -- Width: 14cm
- -- Height: 15cm
- - Bar Dimensions
- -- Width: 3cm
- -- Height: 10cm
- -- Depth: 2.5cm
Should not have
- We do not want to have an 3 dimensional images or objects. Nor do we want to have product images and any imagery should be only to give the impression of the flavours within rather than an image of the flavour. Finally, we do not want to have gradients included in the design.

```html
<!DOCTYPE html>
<html lang="en">
<head>
<meta charset="utf-8">
<title>MunchWell Bar Wrappers</title>
<link rel="stylesheet" href="https://fonts.googleapis.com/css2?family=Bowlby+One&family=Nunito:wght@800;900&family=Patrick+Hand&display=swap">
<style>
  :root {
    --page: #ffffff;
    --foil: #f8f8f8;
    --foil-edge: #e1e1e1;
    --crimp: #e6e6e6;
    --ink: #111111;
    --gold: #a5802f;
    --cherry-band: #111111;
    --berry-band: #e8e229;
    --tropic-band: #7fa046;
  }
  * { margin: 0; padding: 0; box-sizing: border-box; }
  html, body { width: 1200px; height: 884px; overflow: hidden; background: var(--page); }
  .lineup { position: relative; width: 1200px; height: 884px; }
  .wrapper {
    position: absolute; top: 126px; width: 186px; height: 556px;
    background: var(--foil); border: 1px solid var(--foil-edge); border-radius: 6px;
    text-align: center; color: var(--ink);
  }
  .wrapper--cherry { left: 280px; }
  .wrapper--berry { left: 520px; }
  .wrapper--tropic { left: 756px; }
  .seal { position: absolute; left: 0; right: 0; height: 40px;
    background: repeating-linear-gradient(90deg, var(--crimp) 0 2px, transparent 2px 6px); }
  .seal--top { top: 0; border-bottom: 1px solid var(--foil-edge); }
  .seal--bottom { bottom: 0; border-top: 1px solid var(--foil-edge); }
  .brand { position: absolute; top: 78px; left: 0; right: 0; display: flex; justify-content: center; align-items: center; gap: 6px;
    font-family: "Nunito", sans-serif; font-weight: 900; font-size: 21px; color: var(--ink); }
  .brand-dot { width: 10px; height: 10px; border-radius: 50%; background: var(--gold); }
  .flavour { position: absolute; top: 162px; left: 10px; right: 10px; transform: rotate(-8deg); }
  .flavour-name { font-family: "Bowlby One", sans-serif; line-height: 0.98; color: var(--ink); }
  .ingredients { display: inline-block; margin-top: 4px; padding: 4px 6px; font-family: "Nunito", sans-serif; font-weight: 900; font-size: 10px; line-height: 1.15; text-align: left; }
  .wrapper--cherry .flavour-name { font-size: 34px; }
  .wrapper--berry .flavour-name { font-size: 28px; }
  .wrapper--tropic .flavour-name { font-size: 31px; }
  .wrapper--cherry .ingredients { background: var(--cherry-band); color: #ffffff; }
  .wrapper--berry .ingredients { background: var(--berry-band); color: var(--ink); }
  .wrapper--tropic .ingredients { background: var(--tropic-band); color: #f4f1c8; }
  .claims { position: absolute; top: 322px; left: 0; right: 0; transform: rotate(-4deg);
    font-family: "Patrick Hand", cursive; font-size: 27px; line-height: 1.05; color: var(--gold); letter-spacing: 0.5px; }
  .portion { position: absolute; top: 486px; left: 0; right: 0; font-family: "Nunito", sans-serif; font-weight: 900; font-size: 12px; }
</style>
</head>
<body>
<main class="lineup">
  <article class="wrapper wrapper--cherry">
    <div class="seal seal--top"></div>
    <div class="brand"><span>MunchWell</span><span class="brand-dot"></span></div>
    <div class="flavour">
      <h2 class="flavour-name">Velvet<br>Harbor</h2>
      <p class="ingredients">Sour Cherry and Choco</p>
    </div>
    <p class="claims">0% ADDITIVES<br>60% NUTS<br>100% NATURAL</p>
    <p class="portion">60G</p>
    <div class="seal seal--bottom"></div>
  </article>
  <article class="wrapper wrapper--berry">
    <div class="seal seal--top"></div>
    <div class="brand"><span>MunchWell</span><span class="brand-dot"></span></div>
    <div class="flavour">
      <h2 class="flavour-name">Plum<br>Fizzaroo</h2>
      <p class="ingredients">Banana, Apricot<br>and Blueberry</p>
    </div>
    <p class="claims">0% ADDITIVES<br>60% NUTS<br>100% NATURAL</p>
    <p class="portion">60G</p>
    <div class="seal seal--bottom"></div>
  </article>
  <article class="wrapper wrapper--tropic">
    <div class="seal seal--top"></div>
    <div class="brand"><span>MunchWell</span><span class="brand-dot"></span></div>
    <div class="flavour">
      <h2 class="flavour-name">Sun<br>Melodia</h2>
      <p class="ingredients">Pineapple, Passionfruit<br>and Kiwi</p>
    </div>
    <p class="claims">0% ADDITIVES<br>60% NUTS<br>100% NATURAL</p>
    <p class="portion">60G</p>
    <div class="seal seal--bottom"></div>
  </article>
</main>
</body>
</html>
```